International Honeymoon Tour Operator needs Business Card

We need to design a business card including our new logo for a new tour operator called Marisol Fenwick Holidays. We would like to also include the text 'Personal Tailor-Made Honeymoons for our Guests at a Lower Cost'. Please Include the following details as well; 'Website: www.marisolfenwickholidays.co.uk'; 'E-mail: tobias@marisolfenwickholidays.co.uk'; 'Mobile: 07914266058'. We would like the design to be compatible with the logo and text. The final design should communicate professionalism, modern and ethical.

We want to business card to be double sided.

We would like to be able to easily adjust the e-mail address and contact number in the future for other employees either through you or ourselves.

Target Market(s)

Brides and grooms aged 18-35 predominantly.

Industry/Entity Type

Business

Colors

Designer to choose colors to be used in the design.

Requirements
Must have
• Logo
Requested Text
Double sided
Nice to have
• Additional colour
The wow factor
Should not have
• Images of currency

```html
<!DOCTYPE html>
<html lang="en">
<head>
<meta charset="utf-8">
<title>Marisol Fenwick Holidays — Business Card</title>
<link rel="stylesheet" href="https://fonts.googleapis.com/css2?family=Questrial&display=swap">
<style>
  :root {
    --backdrop: #d9d9d6;
    --card: #f8f8f5;
    --teal: #3f6f61;
    --leaf: #7cb342;
    --bark: #4a3f37;
    --lime: #a6d13f;
    --sage: #84aca1;
  }
  * { margin: 0; padding: 0; box-sizing: border-box; }
  html, body {
    width: 1200px; height: 1000px; overflow: hidden;
    background: var(--backdrop);
    font-family: "Questrial", "Century Gothic", sans-serif;
  }
  .card {
    position: absolute; left: 100px; top: 215px;
    width: 1000px; height: 570px;
    background: var(--card);
    box-shadow: 0 6px 18px rgba(0,0,0,0.18);
    overflow: hidden;
  }
  .brand {
    position: absolute; left: 62px; top: 66px;
    display: flex; align-items: center; gap: 22px;
  }
  .brand-dot {
    width: 74px; height: 74px; border-radius: 50%;
    background: var(--leaf);
    flex: none;
  }
  .brand-name {
    color: var(--teal);
    font-size: 46px; line-height: 1.02;
    letter-spacing: 0.5px;
    width: 360px;
  }
  .holder {
    position: absolute; right: 92px; top: 148px;
    color: var(--teal); font-size: 50px; letter-spacing: 1px;
  }
  .band {
    position: absolute; left: 0; right: 0; top: 258px; height: 150px;
    background: var(--bark);
  }
  .contacts {
    position: absolute; right: 36px; top: 272px;
    list-style: none;
    color: var(--lime); font-size: 30px; line-height: 40px;
    text-align: right;
  }
  .contacts li { display: flex; justify-content: flex-end; align-items: center; gap: 16px; }
  .contacts svg { width: 26px; height: 26px; flex: none; }
  .tagline {
    position: absolute; left: 44px; top: 432px;
    color: var(--sage); font-size: 31px; line-height: 38px;
    letter-spacing: 0.5px;
  }
</style>
</head>
<body>
  <article class="card">
    <div class="brand">
      <span class="brand-dot" aria-hidden="true"></span>
      <span class="brand-name">Marisol Fenwick Holidays</span>
    </div>

    <div class="holder">Tobias</div>

    <div class="band" aria-hidden="true"></div>

    <ul class="contacts">
      <li>tobias@marisolfenwickholidays.co.uk
        <svg viewBox="0 0 26 26" aria-hidden="true"><rect x="3" y="6" width="20" height="14" fill="none" stroke="#fff" stroke-width="1.8"/><path d="M3 6 L13 14 L23 6" fill="none" stroke="#fff" stroke-width="1.8"/></svg>
      </li>
      <li>07914266058
        <svg viewBox="0 0 26 26" aria-hidden="true"><rect x="7" y="2" width="12" height="22" rx="2" fill="none" stroke="#fff" stroke-width="1.8"/><line x1="11" y1="20" x2="15" y2="20" stroke="#fff" stroke-width="1.6"/></svg>
      </li>
      <li>www.marisolfenwickholidays.co.uk
        <svg viewBox="0 0 26 26" aria-hidden="true"><circle cx="13" cy="13" r="10" fill="none" stroke="#fff" stroke-width="1.8"/><ellipse cx="13" cy="13" rx="4.5" ry="10" fill="none" stroke="#fff" stroke-width="1.4"/><line x1="3" y1="13" x2="23" y2="13" stroke="#fff" stroke-width="1.4"/></svg>
      </li>
    </ul>

    <p class="tagline">Personal Tailor-Made Honeymoons<br>for our Guests at a Lower Cost</p>
  </article>
</body>
</html>
```